New Innovative Counselling and psychotherapy Service needs Business Card design

Keep it simple and professional. On one side, just company name and logo (perhaps in all blue) and maybe a tag line.

On other side (all white) my name and Qualifications in centre

Industry/Entity Type

Health And Wellness

Contact Information for Business Card

Derek Hollis
Counsellor & Psychotherapist
BSc (Psychol.), BA, Dip. (Couns. & Psych.), PG.Cert (CBT), MGVrA, NWTF

I will also require Mobile no, Email and web site address of which I'll pass on to final designer.

Font styles to use
Sans Serif

Requirements
Must have
• My Logo Only and please use the colours in logo that is in it.
Should not have
• Any other images

```html
<!DOCTYPE html>
<html lang="en">
<head>
<meta charset="utf-8">
<title>Brightfield Lane – Business Cards</title>
<link href="https://fonts.googleapis.com/css2?family=Open+Sans:wght@400;600;700&display=swap" rel="stylesheet">
<style>
  :root {
    --page: #eceef0;
    --card: #ffffff;
    --blue: #4fb0e3;
    --blue-faint: #e9f4fb;
    --green: #8cc658;
    --ink: #2b2b2b;
    --white: #ffffff;
  }
  * { box-sizing: border-box; margin: 0; padding: 0; }
  html, body {
    width: 1200px; height: 902px; overflow: hidden;
    background: var(--page);
    font-family: "Open Sans", sans-serif;
  }
  .sheet {
    position: relative; width: 1200px; height: 902px;
    display: flex; flex-direction: column; align-items: center; justify-content: center; gap: 56px;
  }
  .card {
    position: relative; width: 600px; height: 343px;
    background: var(--card); overflow: hidden;
    box-shadow: 0 6px 18px rgba(0,0,0,0.12);
  }
  /* front */
  .card-front { display: flex; flex-direction: column; align-items: center; justify-content: center; gap: 22px; }
  .brand-dot { border-radius: 50%; background: var(--blue); }
  .card-front .brand-dot { width: 96px; height: 96px; }
  .brand-name { color: var(--ink); font-weight: 400; letter-spacing: 0.5px; }
  .card-front .brand-name { font-size: 34px; }

  /* back */
  .back-brand { position: absolute; left: 46px; top: 48px; display: flex; align-items: center; gap: 18px; }
  .back-brand .brand-dot { width: 54px; height: 54px; }
  .back-brand .brand-name { font-size: 30px; }
  .faint-circle {
    position: absolute; right: -30px; top: -60px; width: 200px; height: 200px;
    border-radius: 50%; background: var(--blue-faint);
  }
  .person { position: absolute; left: 100px; top: 178px; }
  .person-name { color: var(--blue); font-weight: 700; font-size: 30px; line-height: 1.1; }
  .person-role { color: var(--ink); font-weight: 600; font-size: 14px; margin-top: 2px; }
  .quals-band {
    position: absolute; left: 0; right: 210px; top: 252px; height: 52px;
    background: var(--blue); color: var(--white);
    padding: 7px 0 0 106px; font-size: 12.5px; line-height: 1.45;
    white-space: nowrap;
  }
  .contact-box {
    position: absolute; right: 0; top: 160px; width: 210px; height: 110px;
    background: var(--green); color: var(--white);
    padding: 14px 0 0 16px; display: flex; flex-direction: column; gap: 8px;
    font-size: 12px; white-space: nowrap;
  }
  .contact-line { display: flex; align-items: center; gap: 9px; }
  .contact-icon { width: 20px; height: 20px; flex: none; }
</style>
</head>
<body>
<main class="sheet">
  <section class="card card-front" aria-label="Front of business card">
    <span class="brand-dot"></span>
    <span class="brand-name">Brightfield Lane</span>
  </section>

  <section class="card card-back" aria-label="Back of business card">
    <span class="faint-circle"></span>
    <div class="back-brand">
      <span class="brand-dot"></span>
      <span class="brand-name">Brightfield Lane</span>
    </div>

    <div class="person">
      <p class="person-name">Derek Hollis</p>
      <p class="person-role">Counsellor &amp; Psychotherapist</p>
    </div>

    <div class="quals-band">
      <p>BSc (Psychol.), BA, Dip. (Couns. &amp; Psych.),</p>
      <p>PG.Cert (CBT), MGVrA, NWTF</p>
    </div>

    <div class="contact-box">
      <p class="contact-line">
        <svg class="contact-icon" viewBox="0 0 20 20" aria-hidden="true">
          <circle cx="10" cy="10" r="9.5" fill="#fff"/>
          <rect x="7" y="4.5" width="6" height="11" rx="1.2" fill="#8cc658"/>
          <rect x="8" y="6" width="4" height="7" fill="#fff"/>
        </svg>
        000 0000 0000
      </p>
      <p class="contact-line">
        <svg class="contact-icon" viewBox="0 0 20 20" aria-hidden="true">
          <circle cx="10" cy="10" r="9.5" fill="#fff"/>
          <rect x="5" y="6.5" width="10" height="7" fill="none" stroke="#8cc658" stroke-width="1.4"/>
          <path d="M5 6.5 L10 11 L15 6.5" fill="none" stroke="#8cc658" stroke-width="1.4"/>
        </svg>
        hello@brightfieldlane.com
      </p>
      <p class="contact-line">
        <svg class="contact-icon" viewBox="0 0 20 20" aria-hidden="true">
          <circle cx="10" cy="10" r="9.5" fill="#fff"/>
          <circle cx="10" cy="10" r="5.5" fill="none" stroke="#8cc658" stroke-width="1.3"/>
          <ellipse cx="10" cy="10" rx="2.4" ry="5.5" fill="none" stroke="#8cc658" stroke-width="1.1"/>
          <path d="M4.5 10 H15.5" stroke="#8cc658" stroke-width="1.1"/>
        </svg>
        brightfieldlane.com
      </p>
    </div>
  </section>
</main>
</body>
</html>
```